Lavish QM Hair Extension Box Design and inside care instructional card/booklet (sample provided)

https://www.filecrate-example.com/sh/pq7rm2kd9vwz4nb/Hx3TqaLpmd is a link to filecrate pictures
am looking for a creative box design. I think it would be nice if the box looked like a highend fashion ad but wrapped around a box. The file must be high resolution so the print work does not look faded which is a critique of my current box attached.
I like the background color to be all black or all white.
I usually am drawn toward Emerald Green and Eggplant colors but I also like clean cut colors like white, gold, or gun metal grey or platinums.
I am open to creative designers thoughts on what looks best. No matter what think HIGH HIGH END.
On the inside we will provide a small (matching) instructional care card tagged to the hair.
Reason: I want to send feedback to current designers and give them adequate time to make changes.
I want to see multiple ethicities on the box.
ALL designers can you take my current box and update the pictures on the front, make it a high vector file, and change the information on the back. Lastly please include the maintenance card.
Target Market(s)
It is for all but I want anyone who holds it to feel like it is the most HIGH END hair and skincare line.
https://www.filecrate-example.com/sh/pq7rm2kd9vwz4nb/Hx3TqaLpmd
Industry/Entity Type
Fashion
Logo Text
Lavish QM
Requirements
Must have
- 1. High Resolution Vector File
2. Must be able to print with sharp image
3. The box needs to look like a no other on the market. I want the packaging to look expensive compared to most.
4. Please be create (I think I want my box to resemble a high end ad wrapped around a box)
5. website on the box:
www.shoplavishqm.com
6. I would like to see social media on the box too (but only if it looks good)
Facebook @LavishQM
Twitter @LavishQM
LavishQM.Pinwheelr.com
7. Inside panel of box (currently all white needs to have one of the logos staggered on the inside pls) or some awesome image like a coupon code or advertisement.
Back Panel of box
Our hair is 100% Verra Human Hair
Our hair comes in Hand Sewn Double Drawn, Hand Sewn Single Drawn, Machine Sewn Double Drawn, Machine Sewn Single Drawn
We provide clip-ins, tape weft, loose strand or braiding hair and weft hair extension. Add faux eye lashes to your look to complete your style.
Information on inside instructional Care Card:
Lavish QM Hair Care Recommendations Manual
Hair extensions must receive proper care to ensure maximum performance.
Washing
1. Wash hair Weekly or Biweekly.
Brush your hair in a downward motion starting at the ends and working your way toward the weft. Remove all tangles before washing it.
Remember that too much of any dirt, sweat, or over use of products can cause the hair to be less manageable.
2. Use moisturizing hair care products like conditioner to keep it soft.
Do not overly condition as it can weigh the hair down. We recommend a nickel size amount for shorter lengths and a quarter size amount for longer lengths.
This step is especially important if you are using clip in hair extensions because the hair will not get any of the moisture from the natural oils your scalp produces.
If you deep condition once a week be sure to rinse thoroughly.
3. Use cool to tepid water.
Daily
1. Do not over heat.
When adding heat remember that it is human hair. And like human hair over heating can cause hair damage.
2. Use a heat protectant.
Whether it’s a blow dryer, curling iron or flat iron, they all have one thing in common: they damage your hair. If you want to make your extensions last, your best bet is to use a heat protectant whenever you use a heated appliance on your hair. This simple step will prevent breakage and keep your locks looking great a lot longer
3. If looking to add moisture and/or shine a dime size amount of moisturizing hair products or serum.
We do not recommend using Instant conditioners or heavy grease on the hair. When finishing your style use only a dime size of any product to avoid weighing the hair down.
Maintenance
1. Though some styles do not require professional treatment we recommend using professional hair care specialist when initially putting any extensions in your hair especially for the first time.
2. Seek a professional to remove extensions
3. Brushing
Use a soft bristle brush. Harsh brushes or overly brushing is not necessary. Love Your Hair! And it will love you back by being manageable, long-lasting, and versatile.
4. Keep ends trimmed. It is real hair and can get split ends. Trim .5 to 1 inch every 8 weeks.
5. Tutorial are provided on our blog at LavishQM.com.
Exercise
1. Gently brush hair up into a ponytail.
2. Wash all chlorine from hair after swimming and use a hair cap. Too much chlorine can decrease longevity of the hair.
Nightly
1. Part hair down the middle. Place in two French braids.
2. Wrap hair and tie with a silk scarf or Delphine-Rue Ashcombe head wrap.
3. Make one long French braid in the back.
4. Never sleep on wet hair. It can cause hair longevity to decrease and become less pliable.
Hair Coloring
1. Professional Hair Care Specialist Only
For maximum performance use Lavish QM Hair Care Products. Shop online at www.ShopLavishQM.com. Tutorials are provided on our blog at www.LavishQM.com.
Like us on Facebook @LavishQM and Twitter @LavishQM
Join our online Soap Opera at TressSaga.pinwheelr.com
Copywright 2014 Lavish QM Spa and Salon
Nice to have
- Elite, Sleek, sexy, and upmarket. The box must include the following information and you do not have to use the attached photos. I can provide others or they can be incorporated. The feedback given about the first box is that Black American clientelle did not see them reflected in the box. We like the idea of having women's images on the box but want the ethnicities to be diverse if used.
Please look at my website www.lavishqm.com to get familiar with the company style.
And proof website of new Product Boutique http://proof.siteforgeonline-example.com/lavishqm/
BE CREATIVE
Feel free to email me at Rosalind@lavishqm.com subject line (Maker Swarm Box)
Should not have
- Red

```html
<!DOCTYPE html>
<html lang="en">
<head>
<meta charset="utf-8">
<title>Lavish QM Hair Extension Box Dieline</title>
<link href="https://fonts.googleapis.com/css2?family=Raleway:wght@200;300;700&family=Roboto+Condensed:wght@300;400;700&display=swap" rel="stylesheet">
<style>
  :root {
    --stage-light: #f1f1f3;
    --stage-dark: #bdbdc2;
    --label: #6a6a6e;
    --box-black: #050506;
    --cut-line: #9a2c86;
    --gold-light: #f2dc9a;
    --gold-mid: #c9a14a;
    --gold-dark: #8a6624;
    --hair-light: #8a6048;
    --hair-dark: #2e1a12;
    --inside-light: #7a6f78;
    --inside-dark: #231c24;
    --white: #ffffff;
    --ink: #1a1208;
    --logo-grey: #8f8f95;
  }
  html, body {
    margin: 0;
    width: 1200px;
    height: 900px;
    overflow: hidden;
  }
  body {
    background: radial-gradient(ellipse at 50% 40%, var(--stage-light) 0%, #dcdce0 55%, var(--stage-dark) 100%);
    font-family: "Roboto Condensed", Arial, sans-serif;
  }
  .dieline { display: block; width: 1200px; height: 900px; }
  .view-label { font-family: "Raleway", Arial, sans-serif; font-weight: 200; font-size: 29px; fill: var(--label); }
  .cut { stroke: var(--cut-line); stroke-width: 0.8; }
  .panel-black { fill: var(--box-black); }
  .brand-mark { font-family: "Roboto Condensed", Arial, sans-serif; font-weight: 300; font-size: 19px; letter-spacing: 5px; fill: var(--logo-grey); }
  .gold-bar-text { font-weight: 700; font-size: 11px; fill: var(--ink); }
  .gold-bar-text .sc { font-size: 9px; }
  .product-line { font-weight: 300; font-size: 12px; fill: var(--white); letter-spacing: 0.5px; }
  .product-name { font-weight: 300; font-size: 14px; fill: var(--white); }
  .back-copy { font-weight: 300; font-size: 10.5px; fill: var(--white); }
  .back-url { font-weight: 700; font-size: 7px; fill: var(--white); }
  .back-address { font-weight: 400; font-size: 6px; fill: var(--white); }
  .window-label { font-family: "Raleway", Arial, sans-serif; font-weight: 300; font-size: 13px; fill: #666; }
  .hero-title { font-family: "Raleway", Arial, sans-serif; font-weight: 200; font-size: 52px; fill: var(--white); letter-spacing: 1px; }
  .hero-sub { font-family: "Raleway", Arial, sans-serif; font-weight: 700; font-size: 19px; fill: var(--white); }
  .hero-tag { font-family: "Raleway", Arial, sans-serif; font-weight: 300; font-size: 8.5px; fill: var(--white); }
  .coupon-label { font-weight: 700; font-size: 9px; fill: var(--white); }
  .coupon-code { font-family: "Raleway", Arial, sans-serif; font-weight: 700; font-size: 18px; fill: var(--white); }
  .inside-mark { font-weight: 300; font-size: 15px; letter-spacing: 4px; fill: #b8b8bd; }
</style>
</head>
<body>
<svg class="dieline" viewBox="0 0 1200 900" xmlns="http://www.w3.org/2000/svg">
  <defs>
    <linearGradient id="gold-bar" x1="0" x2="1" y1="0" y2="0">
      <stop offset="0" stop-color="var(--gold-dark)"/>
      <stop offset="0.3" stop-color="var(--gold-light)"/>
      <stop offset="0.6" stop-color="var(--gold-mid)"/>
      <stop offset="1" stop-color="var(--gold-dark)"/>
    </linearGradient>
    <linearGradient id="hair-photo" x1="0" x2="0.6" y1="0" y2="1">
      <stop offset="0" stop-color="#3a2318"/>
      <stop offset="0.35" stop-color="var(--hair-light)"/>
      <stop offset="0.7" stop-color="#6a4634"/>
      <stop offset="1" stop-color="var(--hair-dark)"/>
    </linearGradient>
    <linearGradient id="inside-photo" x1="0" x2="1" y1="0" y2="1">
      <stop offset="0" stop-color="var(--inside-dark)"/>
      <stop offset="0.4" stop-color="var(--inside-light)"/>
      <stop offset="0.75" stop-color="#4a3f4a"/>
      <stop offset="1" stop-color="var(--inside-dark)"/>
    </linearGradient>
    <radialGradient id="portrait-tone" cx="0.45" cy="0.45" r="0.55">
      <stop offset="0" stop-color="#b59a8e"/>
      <stop offset="0.6" stop-color="#6b5a5e"/>
      <stop offset="1" stop-color="#2a2229"/>
    </radialGradient>
    <radialGradient id="bloom-tone" cx="0.5" cy="0.5" r="0.5">
      <stop offset="0" stop-color="#c75a62"/>
      <stop offset="1" stop-color="#c75a62" stop-opacity="0"/>
    </radialGradient>
  </defs>

  <text class="view-label" x="196" y="72">outside</text>
  <text class="view-label" x="770" y="72">inside</text>

  <!-- OUTSIDE DIELINE -->
  <g class="box-outside">
    <path class="panel-black cut" d="M172,118 L193,108 L193,790 L172,780 Z"/>
    <rect class="panel-black cut" x="193" y="108" width="152" height="682"/>
    <path class="panel-black cut" d="M193,790 L345,790 L345,850 Q345,862 333,862 L205,862 Q193,862 193,850 Z"/>
    <path class="panel-black cut" d="M345,108 L350,68 L385,68 L390,108 Z"/>
    <rect class="panel-black cut" x="345" y="108" width="45" height="682"/>
    <path class="panel-black cut" d="M345,790 L390,790 L385,825 L350,825 Z"/>
    <path class="panel-black cut" d="M390,108 L390,45 Q390,33 402,33 L528,33 Q540,33 540,45 L540,108 Z"/>
    <line class="cut" x1="390" y1="64" x2="540" y2="64"/>
    <rect class="panel-black cut" x="390" y="108" width="150" height="682"/>
    <path class="panel-black cut" d="M540,108 L545,68 L578,68 L583,108 Z"/>
    <rect class="panel-black cut" x="540" y="108" width="43" height="682"/>
    <path class="panel-black cut" d="M540,790 L583,790 L578,825 L545,825 Z"/>

    <!-- back panel -->
    <text class="brand-mark" x="269" y="163" text-anchor="middle">LAVISH QM</text>
    <rect x="193" y="208" width="152" height="25" fill="url(#gold-bar)"/>
    <text class="gold-bar-text" x="269" y="224" text-anchor="middle">100% P<tspan class="sc">REMIUM</tspan> H<tspan class="sc">UMAN</tspan> H<tspan class="sc">AIR</tspan></text>
    <text class="product-line" x="269" y="262" text-anchor="middle">VERRA HAIR</text>
    <text class="product-name" x="269" y="281" text-anchor="middle">8” CURLY HAIR</text>
    <text class="back-copy" text-anchor="middle">
      <tspan x="269" y="345">Our hair is 100% Verra</tspan>
      <tspan x="269" y="358">Human Hair</tspan>
      <tspan x="269" y="385">Our hair comes in Hand</tspan>
      <tspan x="269" y="398">Sewn Double Drawn,</tspan>
      <tspan x="269" y="411">Hand Sewn Single Drawn,</tspan>
      <tspan x="269" y="424">Machine Sewn Double</tspan>
      <tspan x="269" y="437">Drawn, Machine Sewn</tspan>
      <tspan x="269" y="450">Single Drawn</tspan>
      <tspan x="269" y="477">We provide clip-ins, tape</tspan>
      <tspan x="269" y="490">weft, loose strand or</tspan>
      <tspan x="269" y="503">braiding hair and weft</tspan>
      <tspan x="269" y="516">hair extension. Add faux</tspan>
      <tspan x="269" y="529">eye lashes to your look to</tspan>
      <tspan x="269" y="542">complete your style.</tspan>
    </text>
    <text class="back-url" x="269" y="712" text-anchor="middle">WWW.SHOPLAVISHQM.COM</text>
    <text class="back-address" text-anchor="middle">
      <tspan x="269" y="737">412 East Larkmoor Lane</tspan>
      <tspan x="269" y="745">Suite 220-318</tspan>
      <tspan x="269" y="753">Fernvale, AZ 85099</tspan>
    </text>

    <!-- front panel -->
    <text class="brand-mark" x="465" y="163" text-anchor="middle">LAVISH QM</text>
    <rect x="390" y="205" width="150" height="513" fill="url(#hair-photo)" role="img" aria-label="Photograph of a woman's shoulder with long brown curly hair"/>
    <path fill="var(--white)" d="M439,270 C434,360 420,430 416,520 C412,610 440,656 472,656 C506,656 522,624 518,585 C513,530 472,505 456,445 C445,395 441,330 439,270 Z"/>
    <text class="window-label" x="466" y="565" text-anchor="middle">window</text>
    <rect x="390" y="718" width="150" height="25" fill="url(#gold-bar)"/>
    <text class="gold-bar-text" x="465" y="734" text-anchor="middle">100% P<tspan class="sc">REMIUM</tspan> H<tspan class="sc">UMAN</tspan> H<tspan class="sc">AIR</tspan></text>
    <text class="product-line" x="465" y="761" text-anchor="middle">VERRA HAIR</text>
    <text class="product-name" x="465" y="777" text-anchor="middle">8” CURLY HAIR</text>
  </g>

  <!-- INSIDE DIELINE -->
  <g class="box-inside">
    <path fill="url(#inside-photo)" class="cut" d="M693,140 L713,130 L713,108 L855,108 L855,98 L897,98 L897,74 Q897,62 909,62 L1025,62 Q1037,62 1037,74 L1037,98 L1073,98 L1078,130 L1078,800 L1040,800 L1040,790 L897,790 L897,803 L855,803 L855,790 L855,826 Q855,838 843,838 L725,838 Q713,838 713,826 L713,790 L693,780 Z" role="img" aria-label="Photograph of long dark curly hair spreading across the inside of the box"/>
    <rect x="693" y="135" width="162" height="655" fill="url(#portrait-tone)" role="img" aria-label="Portrait photograph of a woman with eyes closed, holding a pink gerbera daisy"/>
    <ellipse cx="830" cy="640" rx="95" ry="75" fill="url(#bloom-tone)"/>
    <g class="cut" fill="none">
      <line x1="713" y1="130" x2="713" y2="790"/>
      <line x1="855" y1="108" x2="855" y2="803"/>
      <line x1="897" y1="98" x2="897" y2="803"/>
      <line x1="1040" y1="98" x2="1040" y2="800"/>
      <line x1="897" y1="98" x2="1037" y2="98"/>
      <line x1="713" y1="790" x2="855" y2="790"/>
      <line x1="897" y1="132" x2="1037" y2="132"/>
    </g>
    <text class="hero-title" x="907" y="195">HAIR</text>
    <text class="hero-sub" x="908" y="214">EXTENSIONS</text>
    <line x1="908" y1="220" x2="1030" y2="220" stroke="var(--white)" stroke-width="1"/>
    <text class="hero-tag" text-anchor="middle">
      <tspan x="968" y="232">Get the look, leght, and color</tspan>
      <tspan x="968" y="243">you always wanted</tspan>
    </text>
    <path fill="var(--white)" d="M941,288 C936,375 922,445 918,530 C914,610 942,642 973,642 C1006,642 1021,612 1018,575 C1013,525 975,500 959,445 C948,400 943,345 941,288 Z"/>
    <text class="window-label" x="968" y="570" text-anchor="middle">window</text>
    <text class="coupon-label" x="967" y="716" text-anchor="middle">COUPON CODE</text>
    <text class="coupon-code" x="967" y="736" text-anchor="middle">BEAUTYHAIR</text>
    <text class="inside-mark" x="767" y="740" text-anchor="middle">LAVISH QM</text>
  </g>
</svg>
</body>
</html>
```